VALMIKE GROUP

This is a company that provides executive protection. Our motto is "New Era in Protection"... I don't want this to look like other security websites. I want it to be clean and sharp and represent a new era. We are based in the bay area so maybe a picture of San Francisco in the background?
I want it to be able to funnel down a couple different categories.
1. About Us
2. Services (Executive Protection, Covert Protection, Residential Protection & Intelligence)
3. Iron Finch (Training & Consulting)
4. Contact Us
I want it to be very clean and modern. I don't want there to be any pictures of bodyguards with ear pieces like every other website.
Target Market(s)
Ultra High Net Worth Individuals
Coding
Coded - Design and coding required
Number of Pages Required
1 page
Requirements
Must have
- Colors of my Symbol
Nice to have
- City in the background, San Francisco, New York or the Pinehallow Club in Montana.
Should not have
- Should not look like an KVM website or have photos of bodyguards. I want this to be a clean and simple website with my logo

```html
<!DOCTYPE html>
<html lang="en">
<head>
<meta charset="utf-8">
<title>VALMIKE GROUP — New Era in Protection</title>
<link rel="stylesheet" href="https://fonts.googleapis.com/css2?family=Poppins:wght@300;400;500;600;700;800&display=swap">
<style>
:root{
  --brand:#8a1020;
  --brand-dark:#6e0c18;
  --ink:#444;
  --ink-soft:#555;
  --white:#fff;
  --night:#1b1f36;
  --footer:#1e1f24;
}
*{box-sizing:border-box;margin:0;padding:0}
html,body{width:1200px;height:2699px;overflow:hidden}
body{font-family:'Poppins',sans-serif;color:var(--ink);background:var(--white);position:relative}
.abs{position:absolute}
.btn{position:absolute;background:var(--brand);color:var(--white);border-radius:22px;font-weight:500;display:flex;align-items:center;justify-content:center}

/* hero */
.hero{left:0;top:0;width:1200px;height:663px;background:linear-gradient(180deg,#3a1f6e 0%,#b02a55 22%,#e0603f 34%,#2a2d4e 52%,#17324a 75%,#0f2137 100%)}
.hero-photo{position:absolute;inset:0;background:radial-gradient(ellipse 420px 260px at 300px 520px,rgba(230,90,30,.55),transparent 70%),radial-gradient(ellipse 500px 180px at 850px 330px,rgba(255,190,90,.25),transparent 70%)}
.help{right:112px;top:12px;font-size:14px;color:var(--white)}
.help b{font-weight:700;margin-left:8px;font-size:15px}
.navbar{left:267px;top:45px;width:821px;height:54px;background:var(--white)}
.nav-link{position:absolute;top:17px;font-size:15.5px;color:#444}
.nav-link.active{color:var(--brand);font-weight:500}
.nav-underline{position:absolute;left:110px;top:48px;width:65px;height:6px;background:var(--brand)}
.nav-cta{left:918px;top:52px;width:163px;height:40px;font-size:17px}
.logo-box{left:111px;top:0;width:156px;height:136px;background:var(--white);display:flex;flex-direction:column;align-items:center;justify-content:center;gap:8px}
.logo-box .mark{width:34px;height:34px;background:var(--brand)}
.logo-box .name{font-size:17px;font-weight:700;color:#222;letter-spacing:.5px}
.hero-title{left:0;width:1200px;top:310px;text-align:center;font-size:68px;font-weight:800;color:var(--white)}
.hero-sub{left:0;width:1200px;top:405px;text-align:center;font-size:26px;color:var(--white)}
.hero-cta{left:519px;top:453px;width:162px;height:37px;font-size:17px}
.dot{position:absolute;top:618px;width:16px;height:16px;border:2px solid var(--white);border-radius:50%}
.dot.on{background:var(--white);box-shadow:inset 0 0 0 3px #333;width:20px;height:20px;top:616px}

/* intro blocks */
.heading-mark{width:64px;height:64px;background:var(--brand)}
.kicker{font-size:18px;color:#555}
.big{font-size:35px;font-weight:600;color:#555;letter-spacing:.5px}
.para{left:233px;width:734px;text-align:center;font-size:14.5px;line-height:22.3px;color:var(--ink-soft)}
.read{left:519px;width:162px;height:40px;font-size:18px}

/* offers */
.offer{left:0;top:1068px;width:1200px;height:607px;overflow:hidden}
.offer-title{left:0;width:1200px;top:1122px;text-align:center;font-size:33px;font-weight:700;color:var(--white)}
.card{position:absolute;top:1203px;width:318px;height:408px;overflow:hidden}
.card .label{position:absolute;left:29px;font-size:18px;font-weight:600;color:var(--white);line-height:29px}
.card-red{background:linear-gradient(180deg,#7a1a2a,#8c1221);box-shadow:0 4px 10px rgba(0,0,0,.3)}
.card-red h3{position:absolute;top:104px;width:100%;text-align:center;font-size:18px;font-weight:600;color:var(--white)}
.card-red p{position:absolute;top:135px;left:20px;width:278px;text-align:center;font-size:13.5px;line-height:21.3px;color:var(--white)}
.card-red .ghost{position:absolute;left:91px;top:258px;width:136px;height:40px;border:1px solid var(--white);border-radius:20px;color:var(--white);font-size:15px;font-weight:600;display:flex;align-items:center;justify-content:center}

/* subscribe */
.subscribe{left:0;top:1675px;width:1200px;height:372px;background:linear-gradient(180deg,#2b3340 0%,#3f4450 55%,#2a3038 100%)}
.sub-title{left:0;width:1200px;top:1760px;text-align:center;font-size:43px;font-weight:700;color:var(--white)}
.sub-line{left:0;width:1200px;top:1828px;text-align:center;font-size:32px;color:var(--white)}
.field{left:288px;top:1893px;width:624px;height:57px;background:var(--white);border-radius:29px}
.field span{position:absolute;left:22px;top:19px;font-size:14px;color:#777}
.submit{left:691px;top:1893px;width:221px;height:57px;border-radius:29px;font-size:22px;font-weight:600;gap:18px}

/* footer */
.footer{left:0;top:2471px;width:1200px;height:228px;background:var(--footer);color:var(--white)}
.f-logo{left:111px;top:2510px;display:flex;align-items:center;gap:16px}
.f-logo .mark{width:70px;height:70px;border:5px solid var(--white)}
.f-logo .name{font-size:34px;font-weight:700;letter-spacing:1px}
.social{position:absolute;top:2612px;width:25px;height:25px;border-radius:50%;background:var(--white)}
.copy{left:109px;top:2655px;font-size:13.5px}
.f-col{position:absolute;top:2502px;font-size:15.5px;line-height:24px}
.f-col h4{font-size:18px;font-weight:500;margin-bottom:12px}
</style>
</head>
<body>

<!-- hero -->
<section class="abs hero" role="img" aria-label="Night view of San Francisco skyline with the Bay Bridge lit in red and orange">
  <div class="hero-photo"></div>
</section>
<div class="abs help">Need a help? <b>415-555-0182</b></div>
<nav class="abs navbar">
  <span class="nav-link active" style="left:119px">Home</span>
  <span class="nav-underline"></span>
  <span class="nav-link" style="left:207px">About Us</span>
  <span class="nav-link" style="left:319px">Services</span>
  <span class="nav-link" style="left:426px">Iron Finch</span>
  <span class="nav-link" style="left:531px">Contact us</span>
</nav>
<div class="btn nav-cta">Get A Quote</div>
<div class="abs logo-box"><span class="mark"></span><span class="name">VALMIKE</span></div>
<h1 class="abs hero-title">New Era in Protection</h1>
<p class="abs hero-sub">We provide executive protection.</p>
<div class="btn hero-cta">Get A Quote</div>
<span class="dot" style="left:564px"></span>
<span class="dot on" style="left:590px"></span>
<span class="dot" style="left:621px"></span>

<!-- welcome -->
<div class="abs heading-mark" style="left:421px;top:722px"></div>
<div class="abs kicker" style="left:512px;top:722px">Welcome to</div>
<div class="abs big" style="left:510px;top:750px">VALMIKE GROUP</div>
<p class="abs para" style="top:816px">Lorem Ipsum is simply dummy text of the printing and typesetting industry. Lorem Ipsum has been the industry's standard dummy text ever since the 1500s, when an unknown printer took a galley of type and scrambled it to make a type specimen book. It has survived not only five centuries, but also the leap into electronic typesetting, remaining essentially unchanged. It was popularised in the 1960s with the release of Letraset sheets containing Lorem Ipsum passages, and more recently with desktop publishing software like Aldus PageMaker including versions of Lorem Ipsum.</p>
<div class="btn read" style="top:968px">Read more</div>

<!-- offers -->
<svg class="abs offer" viewBox="0 0 1200 607" aria-hidden="true">
  <defs>
    <linearGradient id="dusk" x1="0" y1="0" x2="0" y2="1">
      <stop offset="0" stop-color="#2a3a52"/>
      <stop offset=".55" stop-color="#6a5560"/>
      <stop offset="1" stop-color="#e6901e"/>
    </linearGradient>
  </defs>
  <path d="M0 0H1200V240L1100 260Q600 90 100 252L0 262Z" fill="url(#dusk)" role="img" aria-label="Bay Bridge at dusk with warm sunset sky"/>
</svg>
<h2 class="abs offer-title">VALMIKE GROUP OFFER</h2>
<div class="card" style="left:112px;background:linear-gradient(180deg,#2a3034,#121619)" role="img" aria-label="Thumbprint scan on a raised thumb">
  <span class="label" style="top:357px">Executive Protection</span>
</div>
<div class="card card-red" style="left:439px">
  <h3>Covert Protection</h3>
  <p>Lorem Ipsum is simply dummy text of the printing and typesetting industry. Lorem Ipsum has been the industry's standard dummy text ever since the 1500s, when an unknown printer took a galley</p>
  <span class="ghost">Read More</span>
</div>
<div class="card" style="left:767px;background:linear-gradient(180deg,#0c2a78,#0a1c4e 70%,#081230)" role="img" aria-label="Glowing blue digital illustration of a smart house">
  <span class="label" style="top:324px">Residential Protection &amp;<br>Intelligence</span>
</div>

<!-- subscribe -->
<section class="abs subscribe" role="img" aria-label="Daytime San Francisco downtown skyline"></section>
<h2 class="abs sub-title">Neque porro quisquam est qui dolorem</h2>
<p class="abs sub-line">Subscribe to our mailing list</p>
<div class="abs field"><span>Your Email Address</span></div>
<div class="btn submit">Submit
  <svg width="32" height="28" viewBox="0 0 32 28" aria-hidden="true"><path d="M1 13L31 1 25 27 15 19 26 7 11 17Z" fill="#fff"/><path d="M11 17L13 26 15 19" fill="#ddd"/></svg>
</div>

<!-- iron finch -->
<div class="abs heading-mark" style="left:480px;top:2117px"></div>
<div class="abs kicker" style="left:570px;top:2117px">Valmike Group</div>
<div class="abs big" style="left:568px;top:2145px">IRON FINCH</div>
<p class="abs para" style="top:2211px">Lorem Ipsum is simply dummy text of the printing and typesetting industry. Lorem Ipsum has been the industry's standard dummy text ever since the 1500s, when an unknown printer took a galley of type and scrambled it to make a type specimen book. It has survived not only five centuries, but also the leap into electronic typesetting, remaining essentially unchanged. It was popularised in the 1960s with the release of Letraset sheets containing Lorem Ipsum passages, and more recently with desktop publishing software like Aldus PageMaker including versions of Lorem Ipsum.</p>
<div class="btn read" style="top:2362px">Read more</div>

<!-- footer -->
<footer class="abs footer"></footer>
<div class="abs f-logo" style="color:#fff"><span class="mark"></span><span class="name">VALMIKE</span></div>
<span class="social" style="left:111px" aria-label="Social link"></span>
<span class="social" style="left:144px" aria-label="Social link"></span>
<span class="social" style="left:176px" aria-label="Social link"></span>
<span class="social" style="left:208px" aria-label="Social link"></span>
<div class="abs copy" style="color:#fff">Valmike Group &nbsp;© 2021.All Rights Reserved.</div>
<div class="f-col" style="left:481px;color:#fff"><h4>Quick Links</h4>Home<br>About Us<br>Services<br>Iron Finch<br>Contact us</div>
<div class="f-col" style="left:647px;color:#fff"><h4>Services</h4>Executive Protection<br>Covert Protection<br>Residential Protection<br>&amp; Intelligence</div>
<div class="f-col" style="left:858px;color:#fff;line-height:24px"><h4>To Reach US</h4>415-555-0182<br><span style="display:block;margin-top:8px">hello@valmikegroup.example</span><span style="display:block;margin-top:10px">2140 Harbor Light Way, Oakland,<br>California, 94607.</span></div>

</body>
</html>
```